Bref créative
Double sided A5 leaflet design required - HalvenEstates.co.uk
www.halvenestates.co.uk - Real Estate Company requires a leaflet designed
We need a double sided A5-leaflet designed for our company. We are a commercial estate agent ( commercial real estate agent ). We rent and sell commercial property in Central London.
Real Estate
Landlords or owners for commercial property, who want to sell or rent their commercial property.
professional, corporate,
We will post the leaflets to landlords and owners who want to rent or sell their commercial property in Central London. We want to convince them to use us to sell or rent their commercial property.
Text and inspiration for leaflet
logos

```html
<!DOCTYPE html>
<html lang="en">
<head>
<meta charset="utf-8">
<title>Halven Estates – Selling or Letting Your Commercial Property</title>
<link rel="stylesheet" href="https://fonts.googleapis.com/css2?family=Cinzel:wght@700&family=Open+Sans:wght@400;600&display=swap">
<style>
  :root {
    --page-bg: #ecebe8;
    --sky-top: #6f9cc9;
    --sky-mid: #a9c6e2;
    --building: #c9d6e2;
    --pool: #3f8fa6;
    --pool-deep: #2a6f88;
    --panel: rgba(255, 255, 255, 0.8);
    --navy: #1f3a6e;
    --brand-blue: #2e4f8a;
    --body-text: #3a3a3a;
    --keys-dark: #2b2b2b;
    --keys-light: #9a9ea3;
  }
  * { box-sizing: border-box; margin: 0; padding: 0; }
  html, body {
    width: 1200px; height: 811px; overflow: hidden;
    background: var(--page-bg);
  }
  .leaflet {
    position: absolute; left: 71px; top: 19px;
    width: 1058px; height: 773px;
    overflow: hidden;
  }
  .leaflet__photo {
    position: absolute; inset: 0;
    background:
      linear-gradient(180deg, transparent 0%, transparent 68%, var(--pool) 80%, var(--pool-deep) 100%),
      radial-gradient(ellipse at 62% 40%, var(--building) 0%, rgba(201,214,226,0.6) 30%, transparent 60%),
      linear-gradient(180deg, var(--sky-top) 0%, var(--sky-mid) 60%);
  }
  .panel {
    position: absolute; left: 44px; top: 38px;
    width: 960px; height: 706px;
    background: var(--panel);
    border-radius: 24px;
  }
  .brand {
    position: absolute; left: 60px; top: 32px;
    width: 260px; text-align: center;
  }
  .brand__mark {
    display: block; margin: 0 auto 18px;
    width: 110px; height: 110px; border-radius: 50%;
    background: var(--brand-blue);
  }
  .brand__name {
    font-family: "Open Sans", sans-serif; font-weight: 400;
    font-size: 22px; letter-spacing: 5px;
    color: var(--brand-blue);
  }
  .headline {
    position: absolute; left: 400px; top: 112px;
    width: 540px; text-align: center;
    font-family: "Cinzel", serif; font-weight: 700;
    font-size: 31px; line-height: 40px;
    color: var(--navy);
    text-shadow: 2px 2px 3px rgba(0,0,0,0.35);
  }
  .intro {
    position: absolute; left: 22px; top: 282px;
    width: 920px;
    font-family: "Open Sans", sans-serif; font-weight: 400;
    font-size: 25px; line-height: 32px;
    color: var(--body-text);
  }
  .keys {
    position: absolute; left: 588px; top: 470px;
    width: 300px; height: 150px;
    border-radius: 16px;
    background: linear-gradient(120deg, var(--keys-light) 0%, var(--keys-dark) 70%);
    opacity: 0.85;
  }
  .contact {
    position: absolute; left: 22px; top: 570px;
    font-family: "Open Sans", sans-serif; font-size: 18px; line-height: 26px;
    color: var(--body-text);
  }
</style>
</head>
<body>
  <main class="leaflet">
    <div class="leaflet__photo" role="img" aria-label="Photograph of a modern glass office building under a blue sky with a swimming pool in the foreground"></div>
    <section class="panel">
      <div class="brand">
        <span class="brand__mark"></span>
        <p class="brand__name">HALVEN ESTATES</p>
      </div>
      <h1 class="headline">Selling or Letting Your<br>Commercial Property</h1>
      <p class="intro">Halven Estates is a Commercial Estate Agent specializing in the accquisition anddisposal of commercial property in the Central London. We offer expert advice and Services in all property spheres. Our team can cater to your every need. including commercial sales, lettings, property management and a wide range of bespo ke services.</p>
      <div class="keys" role="img" aria-label="Photograph of a set of keys on a house-shaped key fob"></div>
      <address class="contact" style="font-style: normal;">
        18 Carrow Lane | Fitzrovia | London | W1T 9QX<br>
        T: 020 7946 0000 | F: 020 7946 0001<br>
        E: info@halvenestates.co.uk
      </address>
    </section>
  </main>
</body>
</html>
```